promotional flyer for Valtera Gym

we are after a double sided a5 leaflet to promote our gym, this is to go out to the general public to entice them into getting membership.

gym membership is £30 per month

it should also include the offer of - if you present this leaflet then there will be no joining fee

some of the features of the gym include

strength machines
cardio machines
functional area
sprung floor mat area

Target Market(s)

Adults 16+ who want to go to the gym and workout

Industry/Entity Type

Gym

Font styles to use
Other font styles liked:
• montserrat Regular

Requirements
Must have
• Clean on brand design
• use images supplied by us
Nice to have
• focus on an inclusive experience as the gym will be advertised to everyone
• should also use our "fitter, stronger, Healthier"

```html
<!DOCTYPE html>
<html lang="en">
<head>
<meta charset="utf-8">
<title>Valtera Gym – A5 Leaflet</title>
<link rel="stylesheet" href="https://fonts.googleapis.com/css2?family=Montserrat:wght@400;500;600;700&display=swap">
<style>
  :root {
    --backdrop: #1b1f23;
    --slate: #4f5b66;
    --slate-dark: #434d57;
    --slate-text: #4b5660;
    --orange: #f0572a;
    --orange-deep: #d9481f;
    --paper: #ffffff;
    --photo-light: #e4e5e7;
    --photo-mid: #c4c7cb;
  }
  * { box-sizing: border-box; margin: 0; padding: 0; }
  html, body {
    width: 1200px; height: 1000px; overflow: hidden;
    background: var(--backdrop);
    font-family: "Montserrat", sans-serif;
  }
  .canvas { position: relative; width: 1200px; height: 1000px; }

  .leaflet {
    position: absolute; top: 127px;
    width: 524px; height: 743px; overflow: hidden;
  }
  .leaflet--front { left: 56px; }
  .leaflet--back { left: 618px; }
  .leaflet__art { position: absolute; inset: 0; width: 100%; height: 100%; }

  .brand {
    position: absolute; left: 0; right: 0; text-align: center;
  }
  .brand__name {
    font-weight: 400; font-size: 46px; letter-spacing: 3px; line-height: 1;
    text-transform: uppercase;
  }
  .brand__tagline {
    margin-top: 14px;
    font-weight: 500; font-size: 16px; letter-spacing: 2.4px;
    color: var(--orange); text-transform: uppercase;
  }
  .brand--front { top: 178px; }
  .brand--front .brand__name { color: var(--slate); }
  .brand--back { top: 522px; }
  .brand--back .brand__name { color: var(--paper); }

  .offer {
    position: absolute; left: 200px; width: 318px;
    text-align: center; color: var(--paper);
  }
  .offer__intro { top: 471px; font-size: 14px; font-weight: 700; }
  .offer__price { top: 490px; font-size: 26px; font-weight: 700; }
  .offer__condition { top: 545px; font-size: 27px; font-weight: 400; line-height: 35px; }
  .offer__headline { top: 669px; font-size: 32px; font-weight: 700; }

  .features__heading {
    position: absolute; left: 42px; top: 38px;
    font-size: 19px; font-weight: 700; line-height: 25px;
    color: var(--orange);
  }
  .features__list {
    position: absolute; left: 42px; top: 160px; list-style: none;
  }
  .features__list li {
    position: relative; padding-left: 26px;
    font-size: 18px; font-weight: 500; line-height: 27.5px;
    color: var(--slate-text);
  }
  .features__list li::before {
    content: ""; position: absolute; left: 1px; top: 9px;
    width: 11px; height: 11px; border-radius: 50%;
    background: var(--orange);
  }

  .contact {
    position: absolute; top: 614px;
    font-size: 12.5px; font-weight: 500; line-height: 15.5px;
    color: var(--paper);
  }
  .contact--direct { left: 42px; }
  .contact--address { left: 253px; }
  .contact__label { color: var(--orange); font-weight: 600; }

  .hours {
    position: absolute; left: 42px; top: 666px; width: 440px;
  }
  .hours__title {
    display: flex; align-items: center; gap: 10px;
    font-size: 16px; font-weight: 500; color: var(--orange);
  }
  .hours__title::after {
    content: ""; flex: 1; height: 1px; background: var(--orange);
  }
  .hours__times {
    margin-top: 3px; font-size: 14.5px; font-weight: 500; color: var(--paper);
  }
</style>
</head>
<body>
<main class="canvas">

  <!-- Front -->
  <section class="leaflet leaflet--front">
    <svg class="leaflet__art" viewBox="0 0 524 743" xmlns="http://www.w3.org/2000/svg">
      <defs>
        <linearGradient id="front-photo" x1="0" y1="0" x2="0" y2="1">
          <stop offset="0" stop-color="#f4f4f5"/>
          <stop offset="0.45" stop-color="#e2e3e5"/>
          <stop offset="1" stop-color="#b9bdc1"/>
        </linearGradient>
        <linearGradient id="front-orange" x1="0" y1="0" x2="1" y2="1">
          <stop offset="0" stop-color="#ee6a3d"/>
          <stop offset="1" stop-color="#d9481f"/>
        </linearGradient>
      </defs>
      <rect width="524" height="743" fill="url(#front-photo)" role="img" aria-label="Photo of the gym interior with a woman training among the weight machines"/>
      <path d="M130 743 Q150 360 524 300 L524 743 Z" fill="url(#front-orange)" role="img" aria-label="Photo of dumbbell racks tinted orange"/>
      <path d="M128 743 Q148 356 524 297" fill="none" stroke="var(--slate)" stroke-width="22"/>
      <path d="M146 743 Q164 374 524 314" fill="none" stroke="var(--paper)" stroke-width="2"/>
      <g stroke="var(--slate)" stroke-width="8">
        <circle cx="444" cy="303" r="33" fill="#8a7f86" role="img" aria-label="Photo of a member on a rowing machine"/>
        <circle cx="339" cy="333" r="38" fill="#6b6f5c" role="img" aria-label="Photo of a member at a strength machine"/>
        <circle cx="232" cy="406" r="42" fill="#8c4a3a" role="img" aria-label="Photo of the free weights area"/>
        <circle cx="151" cy="513" r="44" fill="#7a6470" role="img" aria-label="Photo of a member using a shoulder press"/>
        <circle cx="107" cy="648" r="50" fill="#5c4a52" role="img" aria-label="Photo of a spin class"/>
      </g>
      <circle cx="262" cy="105" r="54" fill="none" stroke="var(--slate)" stroke-width="7"/>
    </svg>

    <div class="brand brand--front">
      <p class="brand__name">Valtera Gym</p>
      <p class="brand__tagline">Fitter&nbsp;&nbsp;|&nbsp;&nbsp;Stronger&nbsp;&nbsp;|&nbsp;&nbsp;Healthier</p>
    </div>

    <p class="offer offer__intro">gym membership is</p>
    <p class="offer offer__price">£30 / month</p>
    <p class="offer offer__condition">but if you present<br>this leaflet then<br>there will be</p>
    <p class="offer offer__headline">no joining fee</p>
  </section>

  <!-- Back -->
  <section class="leaflet leaflet--back">
    <svg class="leaflet__art" viewBox="0 0 524 743" xmlns="http://www.w3.org/2000/svg">
      <defs>
        <linearGradient id="back-photo" x1="0" y1="0" x2="1" y2="1">
          <stop offset="0" stop-color="#5d6872"/>
          <stop offset="1" stop-color="#404a54"/>
        </linearGradient>
        <linearGradient id="back-light" x1="0" y1="0" x2="1" y2="1">
          <stop offset="0" stop-color="#d4d6d9"/>
          <stop offset="1" stop-color="#eeeff0"/>
        </linearGradient>
        <linearGradient id="back-band" x1="0" y1="1" x2="1" y2="0">
          <stop offset="0" stop-color="#ee6a3d"/>
          <stop offset="1" stop-color="var(--orange)"/>
        </linearGradient>
      </defs>
      <rect width="524" height="743" fill="url(#back-photo)" role="img" aria-label="Photo of a woman on a spin bike, tinted slate"/>
      <path d="M0 0 L436 0 Q420 380 0 418 Z" fill="url(#back-band)"/>
      <path d="M0 0 L400 0 Q388 356 0 410 Z" fill="var(--slate)"/>
      <path d="M0 0 L396 0 Q384 350 0 404 Z" fill="url(#back-light)" role="img" aria-label="Photo of a woman using a cable machine"/>
      <circle cx="262" cy="445" r="55" fill="none" stroke="var(--paper)" stroke-width="7"/>
    </svg>

    <p class="features__heading">some of<br>the features<br>of the gym<br>include</p>
    <ul class="features__list">
      <li>strength machines</li>
      <li>cardio machines</li>
      <li>functional area</li>
      <li>sprung floor mat area</li>
    </ul>

    <div class="brand brand--back">
      <p class="brand__name">Valtera Gym</p>
      <p class="brand__tagline">Fitter&nbsp;&nbsp;|&nbsp;&nbsp;Stronger&nbsp;&nbsp;|&nbsp;&nbsp;Healthier</p>
    </div>

    <address class="contact contact--direct" style="font-style:normal">
      01632 960415<br>
      www.valteragym.co.uk<br>
      enquiries@valteragym.co.uk
    </address>
    <address class="contact contact--address" style="font-style:normal">
      <span class="contact__label">Valtera Gym</span><br>
      Unit 4 Harbour Parade, Linden Avenue<br>
      Westcombe West Sussex, BN99 4QT
    </address>

    <div class="hours">
      <p class="hours__title">Opening hours</p>
      <p class="hours__times">6am - 10pm mon to Fri | 7am to 7pm Saturday and Sunday</p>
    </div>
  </section>

</main>
</body>
</html>
```